Contractor Plan "B"/Getting Screwed?/Something Useful

We are sending out a series of postcards to a group of local contractors.

The first in the series is: Plan B: Pink Bubble Wrap. Plan A is to buy insurance from my agency. This will be printed, front and back on card stock. We will then glue a piece of bubble wrap to the card and place it in an envelope for delivery.

The second card will be along the same lines but will ask if the client is getting screwed by his current Insurance Company. We will glue a screw in the middle of the card and place the card in an envelope for delivery. On the bottom of we might tell them to call us to get unscrewed.

The third card will follow those lines but say something like: We sent you bubble wrap for your Plan B and you didn't call. Then we sent you something funny but you didn't call. We decided to send you something useful so you might call now! With this card, we are going to send a carpenter pencil.

I am attaching a rough outline of my sketch design for the first card so you will have basic information we will need such as phone number and coverages we offer. If you feel like there is too much info for the size of the card, we can leave some off. I just want the phone to ring! Also, feel free to adjust the wording to make it work better...creative design is not my strong suit!!

I would like for all three cards to be designed. Each can have the same backside. Also, please keep in mind, this is not a postcard so you don't have to leave the blanks on the back for addressing. Each will be mailed in an envelope.

I have also uploaded my logo file as we have recently redone the logo.

Here is more guidance on the project: The cards are going to be 10 cm wide and 23 cm tall. I have added more wording in the brief. Also, I attached a word doc with a good idea of what to use for wording. Basically I want the following idea: Card 1: At top of card - Plan B: Pink Bubble Wrap Below the bubble wrap - Plan A: Call us so you don't have to use Pink Bubble Wrap Card 2: At top of card - Getting Screwed? Is your current agent taking you for granted? Below the area where we are going to glue a screw - Get unscrewed, Call us! Card 3: At top of card - We have the sharpest pencil in town! We will leave space for a carpenter pencil to be attached tot he card. On the other side of the open space - Call us today for the best rates on your insurance!

Please review the attached word doc for an idea of what to put on the back of the card. To be clear, we need three designs for the front of the card and can probably use just one design for the back of all three. If you think we need to have a different design for the back of each, I would like to see your ideas. Thank you for your hard work on these!

Reason: Hi, I am extending the time as I am expecting a few more submissions. Thank you!

Target Market(s)

We are targeting both contractors and truckers with this campaign.

Industry/Entity Type

Insurance

Requirements
Must have
• Clever wording. It needs to be a call to action and doesn't need to have too many specifics.

We also have to have space in the middle to glue the bubble wrap on the first card, the screw in the second and attach the pencil in the third.

```html
<!DOCTYPE html>
<html lang="en">
<head>
<meta charset="utf-8">
<title>Harborline Insurance – Contractor Cards</title>
<link href="https://fonts.googleapis.com/css2?family=Arvo:wght@700&family=Bebas+Neue&family=Nunito+Sans:wght@400;600;700&family=Questrial&display=swap" rel="stylesheet">
<style>
  :root {
    --red: #c01f33;
    --grey: #6d6e71;
    --grey-band: #6f7073;
    --grey-text: #77787b;
    --white: #ffffff;
    --backdrop: #efe6d6;
    --steel: #b9bcc0;
    --pencil: #d9382a;
  }
  * { margin: 0; padding: 0; box-sizing: border-box; }
  html, body { width: 1124px; height: 1200px; overflow: hidden; }
  body { background: var(--backdrop); position: relative; font-family: "Nunito Sans", sans-serif; }

  .card {
    position: absolute;
    background: var(--white);
    box-shadow: 0 2px 6px rgba(0,0,0,.18);
  }
  .card--screw { left: 47px; top: 35px; width: 493px; height: 1132px; }
  .card--pencil { left: 576px; top: 40px; width: 492px; height: 1127px; }

  .headline {
    position: absolute;
    font-family: "Bebas Neue", sans-serif;
    font-weight: 400;
    color: var(--red);
    text-transform: uppercase;
    letter-spacing: 0;
    white-space: nowrap;
  }
  .card--screw .headline { left: 31px; top: 26px; font-size: 140px; line-height: 120px; }
  .card--pencil .headline { left: 109px; top: 22px; font-size: 124px; line-height: 95px; }

  .rule { position: absolute; height: 9px; background: var(--grey); }
  .card--screw .rule { left: 14px; top: 285px; width: 457px; }
  .card--pencil .rule { left: 106px; top: 511px; width: 365px; }

  .subline {
    position: absolute; left: 0; right: 0; top: 316px;
    text-align: center; font-weight: 700; font-size: 27px; line-height: 31px;
    color: var(--grey); letter-spacing: -0.5px;
  }

  .story {
    position: absolute; left: 110px; top: 532px;
    font-family: "Questrial", sans-serif; font-size: 22px; line-height: 31.3px;
    color: var(--grey-text); letter-spacing: -0.4px;
  }

  .object-slot { position: absolute; }
  .card--screw .object-slot {
    left: 92px; top: 450px; width: 305px; height: 245px;
    background: radial-gradient(ellipse at 50% 50%, var(--steel) 0%, #dfe1e3 45%, var(--white) 72%);
  }
  .card--pencil .object-slot {
    left: 27px; top: 20px; width: 52px; height: 725px;
    background: linear-gradient(180deg, #e9dccb 0%, #e7664f 12%, var(--pencil) 100%);
  }

  .call-band {
    position: absolute; left: 0; right: 0; top: 765px; height: 160px;
    background: var(--grey-band); text-align: center;
  }
  .card--pencil .call-band { top: 760px; }
  .call-band__lead {
    margin-top: 20px; font-family: "Questrial", sans-serif; font-size: 38px; line-height: 46px;
    color: var(--white); letter-spacing: -0.3px;
  }
  .call-band__phone {
    margin-top: 10px; font-family: "Arvo", serif; font-weight: 700; font-size: 50px; line-height: 60px;
    color: var(--red); letter-spacing: -1px;
    text-shadow: 2px 0 0 var(--white), -2px 0 0 var(--white), 0 2px 0 var(--white), 0 -2px 0 var(--white);
  }

  .brand {
    position: absolute; left: 0; right: 0; top: 975px; text-align: center;
    font-weight: 700; font-size: 34px; line-height: 40px; color: var(--red); letter-spacing: 1px;
  }
  .card--pencil .brand { top: 970px; }
  .tagline {
    position: absolute; left: 0; right: 0; top: 1033px; text-align: center;
    font-family: "Questrial", sans-serif; font-size: 25px; line-height: 32px; color: var(--grey-text);
  }
  .card--pencil .tagline { top: 1030px; }
  .tagline-rule { position: absolute; top: 1072px; height: 4px; background: var(--red); }
  .card--screw .tagline-rule { left: 25px; width: 447px; }
  .card--pencil .tagline-rule { left: 24px; top: 1068px; width: 447px; }
</style>
</head>
<body>

<section class="card card--screw">
  <h1 class="headline">Getting<br>Screwed?</h1>
  <div class="rule"></div>
  <p class="subline">Is your current insurance company<br>taking you for granted?</p>
  <div class="object-slot" role="img" aria-label="Photo of a silver wood screw"></div>
  <div class="call-band">
    <p class="call-band__lead">Get unscrewed. Call now:</p>
    <p class="call-band__phone">555-014-2290</p>
  </div>
  <p class="brand">HARBORLINE</p>
  <p class="tagline">Your Source For All Things Insurance</p>
  <div class="tagline-rule"></div>
</section>

<section class="card card--pencil">
  <div class="object-slot" role="img" aria-label="Photo of a red carpenter pencil"></div>
  <h1 class="headline">We have<br>the<br>sharpest<br>pencil in<br>town!</h1>
  <div class="rule"></div>
  <p class="story">We sent some bubble wrap,<br>you didn't call.<br>We offered to unscrew you<br>and we didn't hear back.<br>Now, we are sending<br>something useful<br>hoping you will call now...</p>
  <div class="call-band">
    <p class="call-band__lead">For best insurance rates:</p>
    <p class="call-band__phone">555-014-2290</p>
  </div>
  <p class="brand">HARBORLINE</p>
  <p class="tagline">Your Source For All Things Insurance</p>
  <div class="tagline-rule"></div>
</section>

</body>
</html>
```